Design some Business Cards for Consultant

Most of my work is in financial & analytical consulting for microfinance and low-income housing finance, mainly in developing countries (Asia, Africa, Latin America). You can see samples of my published work here: tobiaswenkle.com (main page is the blog; navigate to /papers for other published work).

Looking for a clean, no-nonsense design with limited text (name, city, website, email, skype & phone). Single-sided. Would like to print on recycled paper stock, so consider this in the design. If you can work with a (reasonably priced) online printer that ships to Belgium at reasonable cost, would pay extra for the reference and selection of appropriate paper stock, but this isn't required.

Don't hesitate if you need additional info for your design. Will provide detailed text to the contest winner.

```html
<!DOCTYPE html>
<html lang="en">
<head>
<meta charset="utf-8">
<title>Tobias Wenkle – Business Card</title>
<link rel="stylesheet" href="https://fonts.googleapis.com/css2?family=Source+Sans+3:wght@400;500&display=swap">
<style>
  :root {
    --stage: #000000;
    --paper: #ede6b9;
    --paper-light: #f3edc6;
    --paper-dark: #e4dcac;
    --band: #6b6b6b;
    --name-ink: #1b2150;
    --ink: #111111;
  }
  html, body {
    margin: 0;
    padding: 0;
    width: 1200px;
    height: 713px;
    overflow: hidden;
    background: var(--stage);
  }
  .card {
    position: absolute;
    left: 113px;
    top: 118px;
    width: 891px;
    height: 507px;
    overflow: hidden;
    font-family: "Source Sans 3", "Myriad Pro", sans-serif;
    color: var(--ink);
  }
  .card__paper {
    position: absolute;
    inset: 0;
    background: radial-gradient(ellipse at 40% 30%, var(--paper-light), var(--paper) 55%, var(--paper-dark));
  }
  .card__band {
    position: absolute;
    inset: 0;
  }
  .card__name {
    position: absolute;
    left: 27px;
    top: 12px;
    margin: 0;
    font-size: 38px;
    font-weight: 400;
    color: var(--name-ink);
  }
  .card__role {
    position: absolute;
    left: 27px;
    top: 74px;
    margin: 0;
    font-size: 25px;
    font-weight: 400;
  }
  .card__brand {
    position: absolute;
    left: 690px;
    top: 70px;
    display: flex;
    align-items: center;
    gap: 12px;
  }
  .card__brand-dot {
    width: 52px;
    height: 52px;
    border-radius: 50%;
    border: 3px solid var(--ink);
    box-sizing: border-box;
  }
  .card__brand-name {
    font-size: 30px;
    font-weight: 500;
    color: var(--ink);
  }
  .card__contact,
  .card__address {
    position: absolute;
    margin: 0;
    padding: 0;
    list-style: none;
    font-size: 18.5px;
    line-height: 27px;
  }
  .card__contact { left: 27px; top: 380px; }
  .card__address { left: 378px; top: 388px; }
</style>
</head>
<body>
  <main class="card">
    <div class="card__paper" role="img" aria-label="Recycled cream paper texture"></div>
    <svg class="card__band" width="891" height="507" viewBox="0 0 891 507" aria-hidden="true">
      <polygon points="0,234 891,507 0,507" fill="var(--band)"/>
    </svg>

    <h1 class="card__name">Tobias Wenkle</h1>
    <p class="card__role">Microfinance Consultant</p>

    <div class="card__brand">
      <span class="card__brand-dot"></span>
      <span class="card__brand-name">Wenkle</span>
    </div>

    <ul class="card__contact">
      <li>Tel./fax. your phone</li>
      <li>Mob. your phone</li>
      <li>E-mail. tobias.wenkle@postmail.net</li>
      <li>Blog. http://www.tobiaswenkle.com/</li>
    </ul>

    <ul class="card__address">
      <li>Address.</li>
      <li>your address</li>
      <li>Belgium</li>
    </ul>
  </main>
</body>
</html>
```